UI/ UX Design for ERP Software

We need a new UX/UI interface for a ERP software for property managers. Our CMMS / ERP solution is made based on responsive design technologies and is coded in PHP.
The overall UX to be similar to Tarn Vexa - easy navigation, intuitive menus.

Industry/Entity Type

Property Management

Number of Pages Required

5+ page

Requirements
Must have
• Round dock buttons
Consistent icons across the application
Enough Spacing between buttons/icons/ menu
Consistent Font
Nice to have
• We would like the UX to allow the users to use the application without /minimum training.
Should not have
• we don't want anything that is classic with respect to UX

```html
<!DOCTYPE html>
<html lang="en">
<head>
<meta charset="utf-8">
<title>Nestora – Property ERP screens</title>
<link rel="stylesheet" href="https://fonts.googleapis.com/css2?family=Inter:wght@400;500;600;700&display=swap">
<style>
:root{
  --ink:#1b2430;
  --muted:#5a7ea6;
  --brand:#1e88e5;
  --blue-a:#1fb0ff;
  --blue-b:#0a78f0;
  --orange-a:#ff9a3c;
  --orange-b:#f26a22;
  --tab:#eaf2fb;
  --page-top:#fbfcfe;
  --page-bottom:#f2f6fb;
  --panel:#ffffff;
  --grid:#eef3fa;
  --sun:#f7b500;
}
*{box-sizing:border-box;margin:0;padding:0}
html,body{width:1200px;height:1200px;overflow:hidden}
body{font-family:"Inter",sans-serif;color:var(--ink);background:var(--page-bottom)}
.stage{position:absolute;left:0;top:0;width:1932px;height:1932px;transform:scale(.6211);transform-origin:0 0;
  background:linear-gradient(to bottom,var(--page-top) 0,var(--page-top) 527px,var(--page-bottom) 527px)}
.window{position:absolute;left:247px;width:1439px;border-radius:34px;
  background:linear-gradient(160deg,#ffffff 0%,#f6f9fd 100%);box-shadow:0 18px 50px rgba(40,70,120,.08)}
.window.nav{top:68px;height:765px}
.window.detail{top:884px;height:878px}
.window>*{position:absolute}
.dots{display:flex;gap:8px}
.dots i{width:10px;height:10px;border-radius:50%;display:block}
.dots i:nth-child(1){background:#f7c744}.dots i:nth-child(2){background:#f25757}.dots i:nth-child(3){background:#3ec66d}
.brand{display:flex;align-items:center;gap:8px;font-size:21px;font-weight:700;color:var(--brand)}
.brand b{width:24px;height:24px;background:var(--brand);border-radius:5px;display:block}
.toggle{width:78px;height:30px;border-radius:16px;background:#fff;box-shadow:0 2px 8px rgba(0,0,0,.06)}
.toggle .sun{position:absolute;left:10px;top:6px}
.toggle .moon{position:absolute;right:8px;top:5px;width:20px;height:20px;border-radius:50%;border:3px solid var(--sun)}
.welcome{font-size:15px;transform:translateY(-50%);text-align:right;white-space:nowrap}
.welcome strong{font-weight:600}
.avatar{width:48px;height:48px;border-radius:50%;background:linear-gradient(135deg,#6b4a3a,#2e2a2c);border:2px solid #fff;box-shadow:0 2px 8px rgba(0,0,0,.15)}
.page-title{font-size:21px;font-weight:600;transform:translate(-50%,-50%);white-space:nowrap}
.launcher{background:var(--grid);border-radius:24px;opacity:.8}
.tile{width:74px;height:74px;border-radius:14px;background:#fff;box-shadow:0 4px 14px rgba(40,70,120,.06);
  display:flex;align-items:center;justify-content:center;transform:translate(-50%,-50%)}
.tile svg{width:32px;height:32px;fill:var(--ink)}
.tile-label{font-size:12px;font-weight:500;transform:translate(-50%,-50%);white-space:nowrap}
.dock{width:201px;height:79px;border-radius:16px;background:#fff;box-shadow:0 10px 30px rgba(40,70,120,.08)}
.dock-btn{position:absolute;top:13px;width:52px;height:52px;border-radius:14px;display:flex;align-items:center;justify-content:center}
.dock-btn.home{left:28px;background:linear-gradient(160deg,var(--blue-a),var(--blue-b));box-shadow:0 6px 14px rgba(10,120,240,.3)}
.dock-btn.apps{left:123px;background:linear-gradient(160deg,var(--orange-a),var(--orange-b));box-shadow:0 6px 14px rgba(242,106,34,.3)}
.dock-btn svg{fill:#fff}
.back{width:21px;height:21px;border-radius:50%;background:var(--ink);display:flex;align-items:center;justify-content:center}
.screen-title{font-size:21px;font-weight:600;transform:translateY(-50%)}
.tab{height:39px;border-radius:6px;background:var(--tab);font-size:12px;font-weight:500;display:flex;align-items:center;justify-content:center;white-space:nowrap}
.tab.active{background:linear-gradient(160deg,var(--blue-a),var(--blue-b));color:#fff;font-weight:600;box-shadow:0 6px 14px rgba(10,120,240,.25)}
.card{background:#fff;border-radius:14px;box-shadow:0 6px 24px rgba(40,70,120,.06)}
.card h2{position:absolute;left:30px;top:24px;font-size:18px;font-weight:600}
.edit-link{position:absolute;right:26px;top:26px;display:flex;align-items:center;gap:10px;font-size:12px;font-weight:600;text-decoration:underline}
.fields{position:absolute;left:30px;top:71px;display:grid;grid-template-columns:256px 256px 256px 256px;grid-auto-flow:column;grid-template-rows:repeat(9,41.5px)}
.field dt{font-size:11.5px;font-weight:500;line-height:16px}
.field dd{font-size:11.5px;color:var(--muted);line-height:17px}
.photo{border-radius:8px}
.photo.pool{background:linear-gradient(to bottom,#a9b8d6 0%,#6d7c8e 45%,#3aa4e0 75%,#8fa0ae 100%)}
.photo.roof{background:linear-gradient(to bottom,#5d7fb0 0%,#b7c6da 40%,#3c4654 65%,#6b5a4b 100%)}
</style>
</head>
<body>
<div class="stage">

  <section class="window nav">
    <div class="dots" style="left:49px;top:16px"><i></i><i></i><i></i></div>
    <div class="brand" style="left:50px;top:52px"><b></b>Nestora</div>
    <div class="toggle" style="left:1078px;top:50px">
      <svg class="sun" width="18" height="18" viewBox="0 0 24 24" fill="none" stroke="#f7b500" stroke-width="2.4"><circle cx="12" cy="12" r="5"/><path d="M12 1v3M12 20v3M1 12h3M20 12h3M4.2 4.2l2.1 2.1M17.7 17.7l2.1 2.1M4.2 19.8l2.1-2.1M17.7 6.3l2.1-2.1"/></svg>
      <span class="moon"></span>
    </div>
    <p class="welcome" style="right:109px;top:64px">Welcome, <strong>Lio Marsh</strong></p>
    <div class="avatar" role="img" aria-label="User profile photo" style="left:1347px;top:40px"></div>
    <h1 class="page-title" style="left:719px;top:125px">Start navigation</h1>
    <div class="launcher" style="left:343px;top:147px;width:752px;height:473px"></div>

    <!-- row 1 -->
    <div class="tile" style="left:435px;top:214px"><svg viewBox="0 0 24 24"><circle cx="12" cy="8" r="3.2"/><circle cx="5" cy="9" r="2.4"/><circle cx="19" cy="9" r="2.4"/><path d="M6.5 18c0-3.2 2.5-5.5 5.5-5.5s5.5 2.3 5.5 5.5zM1 17c0-2.4 1.6-4 4-4 1 0 1.6.2 2.2.6C5.9 14.6 5.3 16 5.3 17zM23 17c0-2.4-1.6-4-4-4-1 0-1.6.2-2.2.6 1.3 1 1.9 2.4 1.9 3.4z"/></svg></div>
    <p class="tile-label" style="left:435px;top:263px">Customers</p>
    <div class="tile" style="left:548px;top:214px"><svg viewBox="0 0 24 24"><path d="M5 2h14v20h-5v-4h-4v4H5zM8 5v2h2V5zm6 0v2h2V5zM8 9v2h2V9zm6 0v2h2V9zM8 13v2h2v-2zm6 0v2h2v-2z" fill-rule="evenodd"/></svg></div>
    <p class="tile-label" style="left:548px;top:263px">Properties</p>
    <div class="tile" style="left:665px;top:214px"><svg viewBox="0 0 24 24"><path d="M12 2a10 10 0 100 20 10 10 0 000-20zm0 4a3.5 3.5 0 110 7 3.5 3.5 0 010-7zm0 14a8 8 0 01-6-2.7c.8-1.8 3.1-3 6-3s5.2 1.2 6 3A8 8 0 0112 20z"/></svg></div>
    <p class="tile-label" style="left:665px;top:263px">Tenants</p>
    <div class="tile" style="left:776px;top:214px"><svg viewBox="0 0 24 24"><circle cx="12" cy="7" r="4.5"/><path d="M4 22c0-5 3.6-8 8-8s8 3 8 8z"/></svg></div>
    <p class="tile-label" style="left:776px;top:263px">Contacts</p>
    <div class="tile" style="left:890px;top:214px"><svg viewBox="0 0 24 24"><path d="M9 6l1.4.4.8-1.4 1.8 1-.5 1.5 1 1 1.5-.5 1 1.8-1.4.8.4 1.4-.4 1.4 1.4.8-1 1.8-1.5-.5-1 1 .5 1.5-1.8 1-.8-1.4L9 18l-1.4-.4-.8 1.4-1.8-1 .5-1.5-1-1-1.5.5-1-1.8L3.4 13 3 12l.4-1.4L2 9.8l1-1.8 1.5.5 1-1-.5-1.5 1.8-1 .8 1.4zm0 3.5a2.5 2.5 0 100 5 2.5 2.5 0 000-5z"/><circle cx="18.5" cy="5.5" r="3.5"/><circle cx="18.5" cy="17.5" r="2.8"/></svg></div>
    <p class="tile-label" style="left:890px;top:263px">Contractors</p>
    <div class="tile" style="left:1004px;top:214px"><svg viewBox="0 0 24 24"><circle cx="8" cy="8" r="3.8"/><circle cx="17" cy="8.5" r="3.2"/><path d="M1 20c0-4 3-6.5 7-6.5s7 2.5 7 6.5zM16 20c0-2.4-.8-4.4-2.2-5.8.9-.4 2-.6 3.2-.6 3.4 0 6 2 6 6.4z"/></svg></div>
    <p class="tile-label" style="left:1004px;top:263px">Employees</p>

    <!-- row 2 -->
    <div class="tile" style="left:435px;top:321px"><svg viewBox="0 0 24 24"><path d="M21.5 6.5l-3 3-3-1-1-3 3-3A6 6 0 0010 10l-7.5 7.5a2.1 2.1 0 003 3L13 13a6 6 0 008.5-6.5z"/></svg></div>
    <p class="tile-label" style="left:435px;top:370px">Maintenance</p>
    <div class="tile" style="left:548px;top:321px"><svg viewBox="0 0 24 24"><path d="M9 3h6a2 2 0 012 2v1h4a1 1 0 011 1v5H2V7a1 1 0 011-1h4V5a2 2 0 012-2zm0 2v1h6V5zM2 13.5h8.5V15h3v-1.5H22V20a1 1 0 01-1 1H3a1 1 0 01-1-1z"/></svg></div>
    <p class="tile-label" style="left:548px;top:370px">Works orders</p>
    <div class="tile" style="left:665px;top:321px"><svg viewBox="0 0 24 24"><path d="M11 1h2v2.2c2.3.3 4 1.6 4.6 3.6l-2.2.7C15 6 13.8 5.3 12 5.3c-2 0-3.2.9-3.2 2.1 0 1.2 1 1.8 3.6 2.4 3.2.7 5.4 1.8 5.4 4.7 0 2.3-1.7 4-4.8 4.3V21h-2v-2.2c-2.6-.3-4.5-1.8-5-4l2.3-.6c.4 1.6 1.8 2.5 3.8 2.5 2.2 0 3.4-.9 3.4-2.2 0-1.3-1.1-1.9-3.8-2.5C8.9 11.3 6.7 10.2 6.7 7.5c0-2.2 1.6-3.8 4.3-4.2z"/></svg></div>
    <p class="tile-label" style="left:665px;top:370px">Purchase orders</p>
    <div class="tile" style="left:776px;top:321px"><svg viewBox="0 0 24 24"><path d="M10 2a8 8 0 016.3 12.9l5.4 5.4-2 2-5.4-5.4A8 8 0 1110 2zm0 3a5 5 0 100 10 5 5 0 000-10z"/></svg></div>
    <p class="tile-label" style="left:776px;top:370px">Inspections</p>
    <div class="tile" style="left:890px;top:321px"><svg viewBox="0 0 24 24"><path d="M12 2L23 21H1zm-1.2 6v7h2.4V8zm0 8.5V19h2.4v-2.5z" fill-rule="evenodd"/></svg></div>
    <p class="tile-label" style="left:890px;top:370px">Risk management</p>
    <div class="tile" style="left:1004px;top:321px"><svg viewBox="0 0 24 24"><path d="M9 1h6v2h4v20H5V3h4zm0 2v2h6V3zM8 8v2h2V8zm4 0v2h4V8zm-4 4v2h2v-2zm4 0v2h4v-2zm-4 4v2h2v-2zm4 0v2h4v-2z" fill-rule="evenodd"/></svg></div>
    <p class="tile-label" style="left:1004px;top:370px">Compliance</p>

    <!-- row 3 -->
    <div class="tile" style="left:494px;top:426px"><svg viewBox="0 0 24 24"><path d="M3 3h18v12h-6v6H3zM17 17h4l-4 4z"/></svg></div>
    <p class="tile-label" style="left:494px;top:475px">Tenant requests</p>
    <div class="tile" style="left:610px;top:426px"><svg viewBox="0 0 24 24"><path d="M12 1a1.5 1.5 0 011.5 1.5v.6A7 7 0 0119 10v5l2 3H3l2-3v-5a7 7 0 015.5-6.9v-.6A1.5 1.5 0 0112 1zM9.5 20h5a2.5 2.5 0 01-5 0z"/></svg></div>
    <p class="tile-label" style="left:610px;top:475px">Notifications</p>
    <div class="tile" style="left:725px;top:426px"><svg viewBox="0 0 24 24"><path d="M5 1h9l5 5v17H5zm8 0v6h6zM7 4v1.5h4V4zm0 3v1.5h4V7zm5 4v1c-1.5.3-2.3 1.2-2.3 2.3 0 1.4 1.1 1.9 2.4 2.2.9.2 1.2.4 1.2.8s-.5.7-1.2.7c-.8 0-1.3-.3-1.5-.9l-1.1.4c.2.9 1 1.5 2.5 1.8v1h1v-1c1.5-.3 2.3-1.2 2.3-2.3 0-1.4-1-1.9-2.4-2.2-.9-.2-1.2-.4-1.2-.8s.4-.7 1.1-.7 1.1.3 1.3.8l1.1-.4c-.3-.9-1-1.4-2.2-1.7v-1z" fill-rule="evenodd"/></svg></div>
    <p class="tile-label" style="left:725px;top:475px">Budgeting</p>
    <div class="tile" style="left:837px;top:426px"><svg viewBox="0 0 24 24"><path d="M2 4.5l1.2-1.2 1.3 1.3L7.3 1.8 8.5 3 4.5 7zM10 3.5h12v2.2H10zM2 11.5l1.2-1.2 1.3 1.3 2.8-2.8 1.2 1.2-4 4zM10 10.9h12v2.2H10zM3 17h4v4H3zM10 18h12v2.2H10z"/></svg></div>
    <p class="tile-label" style="left:837px;top:475px">Project mngmt</p>
    <div class="tile" style="left:950px;top:426px"><svg viewBox="0 0 24 24"><path d="M12 1a7 7 0 014.2 12.6c-.8.7-1.2 1.5-1.2 2.4v.5H9V16c0-.9-.4-1.7-1.2-2.4A7 7 0 0112 1zM9 18h6v1.5H9zM10 21h4a2 2 0 01-4 0z"/></svg></div>
    <p class="tile-label" style="left:950px;top:475px">Energy</p>

    <!-- row 4 -->
    <div class="tile" style="left:493px;top:535px"><svg viewBox="0 0 24 24"><path d="M8 1h8l5 5v13H8zM3 6h3v15h11v2H3z"/></svg></div>
    <p class="tile-label" style="left:493px;top:585px">Reports</p>
    <div class="tile" style="left:644px;top:535px"><svg viewBox="0 0 24 24"><path d="M2 3h2v16h18v2H2zM7 11h2v6H7zM10.5 8h2v9h-2zM14 12h2v5h-2zM17.5 6h2v11h-2z"/></svg></div>
    <p class="tile-label" style="left:644px;top:585px">Analytics</p>
    <div class="tile" style="left:799px;top:535px"><svg viewBox="0 0 24 24"><path d="M2 5h20v2H2zM2 11h20v2H2zM2 17h20v2H2zM14 3h3v6h-3zM6 9h3v6H6zM12 15h3v6h-3z"/></svg></div>
    <p class="tile-label" style="left:799px;top:585px">Configuration</p>
    <div class="tile" style="left:951px;top:535px"><svg viewBox="0 0 24 24"><path d="M10 1h4l.6 3 2 .9 2.6-1.7 2.8 2.8-1.7 2.6.9 2 3 .6v4l-3 .6-.9 2 1.7 2.6-2.8 2.8-2.6-1.7-2 .9-.6 3h-4l-.6-3-2-.9-2.6 1.7-2.8-2.8 1.7-2.6-.9-2L1 14v-4l3-.6.9-2-1.7-2.6 2.8-2.8 2.6 1.7 2-.9zm2 7a4 4 0 100 8 4 4 0 000-8z" fill-rule="evenodd"/></svg></div>
    <p class="tile-label" style="left:951px;top:585px">Settings</p>

    <div class="dock" style="left:619px;top:656px">
      <span class="dock-btn home"><svg width="32" height="30" viewBox="0 0 24 22"><path d="M12 1L1 10.5l1.5 1.6L4 10.8V21h6v-6h4v6h6V10.8l1.5 1.3 1.5-1.6z"/></svg></span>
      <span class="dock-btn apps"><svg width="24" height="24" viewBox="0 0 24 24"><circle cx="4" cy="4" r="2.3"/><circle cx="12" cy="4" r="2.3"/><circle cx="20" cy="4" r="2.3"/><circle cx="4" cy="12" r="2.3"/><circle cx="12" cy="12" r="2.3"/><circle cx="20" cy="12" r="2.3"/><circle cx="4" cy="20" r="2.3"/><circle cx="12" cy="20" r="2.3"/><circle cx="20" cy="20" r="2.3"/></svg></span>
    </div>
  </section>

  <section class="window detail">
    <div class="dots" style="left:39px;top:16px"><i></i><i></i><i></i></div>
    <div class="brand" style="left:40px;top:52px"><b></b>Nestora</div>
    <div class="toggle" style="left:1068px;top:49px">
      <svg class="sun" width="18" height="18" viewBox="0 0 24 24" fill="none" stroke="#f7b500" stroke-width="2.4"><circle cx="12" cy="12" r="5"/><path d="M12 1v3M12 20v3M1 12h3M20 12h3M4.2 4.2l2.1 2.1M17.7 17.7l2.1 2.1M4.2 19.8l2.1-2.1M17.7 6.3l2.1-2.1"/></svg>
      <span class="moon"></span>
    </div>
    <p class="welcome" style="right:119px;top:64px">Welcome, <strong>Lio Marsh</strong></p>
    <div class="avatar" role="img" aria-label="User profile photo" style="left:1337px;top:40px"></div>

    <span class="back" style="left:45px;top:112px"><svg width="10" height="10" viewBox="0 0 10 10" fill="none" stroke="#fff" stroke-width="2"><path d="M6.5 1.5L3 5l3.5 3.5"/></svg></span>
    <h1 class="screen-title" style="left:79px;top:122px">Alder Tower</h1>

    <a class="tab active" style="left:47px;top:163px;width:143px">General information</a>
    <a class="tab" style="left:199px;top:163px;width:135px">Organization chart</a>
    <a class="tab" style="left:343px;top:163px;width:92px">Tenant List</a>
    <a class="tab" style="left:444px;top:163px;width:120px">Property Assets</a>
    <a class="tab" style="left:573px;top:163px;width:109px">Contractor list</a>
    <a class="tab" style="left:691px;top:163px;width:136px">Compliance mngmt</a>
    <a class="tab" style="left:836px;top:163px;width:130px">Maint. Work orders</a>
    <a class="tab" style="left:974px;top:163px;width:105px">Work orders</a>
    <a class="tab" style="left:1088px;top:163px;width:116px">Purchase orders</a>
    <a class="tab" style="left:1213px;top:163px;width:76px">Memos</a>
    <a class="tab" style="left:1299px;top:163px;width:71px">Files</a>

    <article class="card" style="left:49px;top:225px;width:1079px;height:467px">
      <h2>General information</h2>
      <a class="edit-link"><svg width="22" height="20" viewBox="0 0 24 22" fill="none" stroke="#1e88e5" stroke-width="2"><path d="M11 4H3v16h16v-8"/><path d="M18 2l3 3-9 9H9v-3z" fill="#1e88e5"/></svg>Property Edit</a>
      <dl class="fields">
        <div class="field"><dt>Province</dt><dd>West Coast Region</dd></div>
        <div class="field"><dt>City</dt><dd>Brookmere</dd></div>
        <div class="field"><dt>Address</dt><dd>42 Harbourline Way, Northvale</dd></div>
        <div class="field"><dt>GPS Addresse</dt><dd>12.4500000 : -45.6700000000001</dd></div>
        <div class="field"><dt>Postal Code</dt><dd>K2R 4T8</dd></div>
        <div class="field"><dt>Date Build</dt><dd>07/01/1980</dd></div>
        <div class="field"><dt>Area (sq.ft)</dt><dd>1500000.00</dd></div>
        <div class="field"><dt>Lot Size</dt><dd>1500000.00</dd></div>
        <div class="field"></div>
        <div class="field"><dt>Zoning</dt><dd>CD1</dd></div>
        <div class="field"><dt>Structure type</dt><dd>Steel and concrete</dd></div>
        <div class="field"><dt>Building height</dt><dd>250 mt</dd></div>
        <div class="field"><dt>Clear height</dt><dd>45 mt</dd></div>
        <div class="field"><dt>Floor loading capacity</dt><dd>50</dd></div>
        <div class="field"><dt>Number of floors</dt><dd>30</dd></div>
        <div class="field"><dt>Number of tenants</dt><dd>30</dd></div>
        <div class="field"><dt>Suites</dt><dd>150</dd></div>
        <div class="field"></div>
        <div class="field"><dt>Typical bay size</dt><dd>-</dd></div>
        <div class="field"><dt>Building envelope</dt><dd>None</dd></div>
        <div class="field"><dt>Parking</dt><dd>Underground + surface</dd></div>
        <div class="field"><dt>Parking ration/N. of stalls</dt><dd>6</dd></div>
        <div class="field"><dt>Sprinkler protected</dt><dd>Yes</dd></div>
        <div class="field"><dt>Sprinkler ESFR</dt><dd>No</dd></div>
        <div class="field"><dt>Sprinkler capacity (gpm)</dt><dd>No</dd></div>
        <div class="field"><dt>Fire alarm panel</dt><dd>Yes</dd></div>
        <div class="field"></div>
        <div class="field"><dt>Fire alarm monitored</dt><dd>Yes</dd></div>
        <div class="field"><dt>Máximum electrical capacity (Amps)</dt><dd>2500</dd></div>
        <div class="field"><dt>Building back-up power source</dt><dd>Yes</dd></div>
        <div class="field"><dt>Number of elevators</dt><dd>30</dd></div>
        <div class="field"><dt>Number of escalators</dt><dd>5</dd></div>
        <div class="field"><dt>Roof construction</dt><dd>EPDM</dd></div>
        <div class="field"><dt>Roof insulation</dt><dd>-</dd></div>
        <div class="field"><dt>Utility meters</dt><dd>-</dd></div>
        <div class="field"><dt>Aditional information</dt><dd>-</dd></div>
      </dl>
    </article>

    <div class="photo pool" role="img" aria-label="Photo of the residential complex with outdoor pool" style="left:1146px;top:226px;width:239px;height:160px"></div>
    <div class="photo roof" role="img" aria-label="Photo of the building's modern cantilevered roof" style="left:1146px;top:405px;width:239px;height:160px"></div>

    <div class="dock" style="left:619px;top:744px">
      <span class="dock-btn home"><svg width="32" height="30" viewBox="0 0 24 22"><path d="M12 1L1 10.5l1.5 1.6L4 10.8V21h6v-6h4v6h6V10.8l1.5 1.3 1.5-1.6z"/></svg></span>
      <span class="dock-btn apps"><svg width="24" height="24" viewBox="0 0 24 24"><circle cx="4" cy="4" r="2.3"/><circle cx="12" cy="4" r="2.3"/><circle cx="20" cy="4" r="2.3"/><circle cx="4" cy="12" r="2.3"/><circle cx="12" cy="12" r="2.3"/><circle cx="20" cy="12" r="2.3"/><circle cx="4" cy="20" r="2.3"/><circle cx="12" cy="20" r="2.3"/><circle cx="20" cy="20" r="2.3"/></svg></span>
    </div>
  </section>

</div>
</body>
</html>
```